Dale Hornsby's Swingcraft Big Band — Hot & Sticky ------ CD Cover Art (and Disc Art)

Need a front cover jacket and a disc design for a fantastic all-pro big band (jazz/funk/reggae) CD. We really want to use a group photo somehow since so many of the band members are world famous, LA's finest studio musicians with mostly original music arranged by the biggest names in jazz. Playful, fun, lighthearted, tasteful arrangements with world class soloists.

Target Market(s)

Music/Jazz/Big band enthusiasts; other musicians

Other font styles liked:
• See uploaded file #4

Colors

Designer to choose colors to be used in the design.

Requirements
Must have
• Legibility . . . must be easy to read and not crowded or cluttered. Font idea below (A Quiet Night Beneath The Tangled Pines) is for feel and flavor. It is absolutely not necessary to match if you have something you like better.
Nice to have
• Colorful but not tacky. Maybe a play on the CD title, Hot and Sticky?

```html
<!DOCTYPE html>
<html lang="en">
<head>
<meta charset="utf-8">
<title>Dale Hornsby's Swingcraft Big Band — Hot &amp; Sticky</title>
<link href="https://fonts.googleapis.com/css2?family=Luckiest+Guy&family=Lato:wght@700&display=swap" rel="stylesheet">
<style>
  :root {
    --paper: #ffffff;
    --ink: #0b0b0b;
    --title-red: #e8141c;
    --paint-yellow: #f9b81a;
    --paint-gold: #fcc72a;
    --paint-orange: #f4561a;
    --paint-red: #ea2a1e;
    --paint-magenta: #b8246e;
    --photo-light: #cfcfcf;
    --photo-mid: #6a6a6a;
    --photo-dark: #2c2c2c;
  }
  html, body {
    margin: 0;
    padding: 0;
    width: 1200px;
    height: 1200px;
    overflow: hidden;
    background: var(--paper);
  }
  .cover {
    position: relative;
    width: 1200px;
    height: 1200px;
    background: var(--paper);
    overflow: hidden;
  }
  .cover-frame {
    position: absolute;
    left: 12px;
    top: 12px;
    width: 1176px;
    height: 1176px;
    border: 1.5px solid var(--ink);
    box-sizing: border-box;
    z-index: 5;
    pointer-events: none;
  }
  .paint-strokes,
  .band-photo,
  .title-art {
    position: absolute;
    left: 0;
    top: 0;
    width: 1200px;
    height: 1200px;
  }
  .band-name,
  .album-title {
    font-family: "Luckiest Guy", Impact, "Arial Black", sans-serif;
    font-weight: 700;
  }
  .band-name { fill: var(--title-red); }
  .album-title { fill: var(--ink); }
  .format-badge {
    position: absolute;
    left: 72px;
    top: 1070px;
    width: 128px;
    height: 80px;
    background: var(--ink);
  }
  .label-mark {
    position: absolute;
    left: 888px;
    top: 1026px;
    width: 250px;
    height: 120px;
    background: var(--ink);
    display: flex;
    align-items: center;
    justify-content: center;
  }
  .label-name {
    font-family: "Lato", Arial, sans-serif;
    font-weight: 700;
    color: var(--paper);
    font-size: 38px;
    line-height: 1.1;
    text-align: center;
  }
</style>
</head>
<body>
<main class="cover">

  <svg class="paint-strokes" viewBox="0 0 1200 1200" role="img" aria-label="Energetic diagonal brush strokes of yellow, orange, red and magenta paint sweeping behind the band">
    <g class="strokes-upper">
      <polygon points="70,520 420,190 540,175 170,510" fill="var(--paint-yellow)"/>
      <polygon points="190,560 560,240 630,232 270,560" fill="var(--paint-magenta)"/>
      <polygon points="250,600 650,230 790,212 390,600" fill="var(--paint-orange)"/>
      <polygon points="380,560 760,200 880,190 500,560" fill="var(--paint-gold)"/>
      <polygon points="470,580 880,240 970,250 590,580" fill="var(--paint-red)"/>
      <polygon points="600,480 1000,230 1090,250 720,490" fill="var(--paint-yellow)"/>
      <polygon points="690,540 1090,300 1110,390 820,540" fill="var(--paint-orange)"/>
      <polygon points="840,580 1100,410 1110,580" fill="var(--paint-gold)"/>
      <polygon points="120,440 300,260 360,250 170,450" fill="var(--paint-orange)"/>
    </g>
    <g class="strokes-lower">
      <polygon points="30,1070 250,960 330,970 40,1130" fill="var(--paint-magenta)"/>
      <polygon points="40,1170 400,960 700,960 300,1190 40,1190" fill="var(--paint-orange)"/>
      <polygon points="180,1190 500,990 630,1000 350,1190" fill="var(--paint-yellow)"/>
      <polygon points="480,1190 850,980 1000,990 700,1190" fill="var(--paint-red)"/>
      <polygon points="700,1190 980,1020 1060,1030 820,1190" fill="var(--paint-orange)"/>
      <polygon points="820,1190 1060,1040 1130,1060 950,1190" fill="var(--paint-gold)"/>
      <polygon points="1000,1010 1188,880 1188,1000 1080,1100" fill="var(--paint-orange)"/>
    </g>
  </svg>

  <svg class="band-photo" viewBox="0 0 1200 1200" role="img" aria-label="Black and white group photo of the big band musicians posing with their trumpets, trombones, saxophones, guitars and bass behind music stands">
    <defs>
      <linearGradient id="photoTone" x1="0" y1="0" x2="0" y2="1">
        <stop offset="0" stop-color="var(--photo-light)"/>
        <stop offset="0.3" stop-color="var(--photo-mid)"/>
        <stop offset="1" stop-color="var(--photo-dark)"/>
      </linearGradient>
    </defs>
    <path d="M12 620 L70 570 L150 510 L250 490 L360 462 L470 470 L560 490 L640 470 L730 478 L820 488 L930 475 L1040 490 L1140 500 L1188 505 L1188 860 L1120 980 L1000 1010 L860 1030 L700 1050 L520 1045 L300 1035 L120 1030 L12 1010 Z" fill="url(#photoTone)"/>
  </svg>

  <svg class="title-art" viewBox="0 0 1200 1200">
    <text class="band-name" x="68" y="152" font-size="58" textLength="1064" lengthAdjust="spacingAndGlyphs">DALE HORNSBY'S SWINGCRAFT BIG BAND</text>
    <text class="album-title" x="138" y="326" font-size="128" textLength="934" lengthAdjust="spacingAndGlyphs">HOT &amp; STICKY</text>
  </svg>

  <div class="format-badge" aria-hidden="true"></div>

  <div class="label-mark">
    <span class="label-name">TALL FERN<br>RECORDS</span>
  </div>

  <div class="cover-frame"></div>
</main>
</body>
</html>
```